Website Design: Business to Business Coaching/Strategy

DO NOT CONTACT ME PRIVATELY. ANY PRIVATE CONTACT WILL BE IGNORED.

I need a website design for a business to business coaching service.

The website is for a company the specializes in coaching/training for other businesses. The business specializes in business development and human resource management.

Where appropriate, please include calls to action, e.g.: book a service & request a quote

CONTENT (SEEE ATTACHMENT)
5 Pages;
1. Home Page with overview of company/services -> Slide show at the top with tagline:

WE HELP MAKE STRATEGY HAPPEN BY

DELIVERING LONG-TERM PERFORMANCE IMPROVEMENTS

SO COMPANIES CAN

"BECOME THE CHANGE THEY WISH TO SEE."

2. Works - core services; coaching; leadership development, workshops
3. Expertise
a. capability: helping people to help themselves
b. company interventions: working in partnership; team facilitation; …
c. testimonials
4. About Us
5. Inquires
a. business capability development and funding
b. Register / enrol for an open programme or workshop
c. client feedback

The website below provides services that are similar to the services of my company: https://www.velcormo.co.uk

DESIGN
- Dark theme matching this style of website BUT a simpler more straightforward design: https://www.duntalwick.ac.uk/
Another theme that I like - Dark themed with a modern/easy design: https://lorpaskins.com/theme-demos/?demo=glimvera-dark

Target Market(s)

Small businesses

Industry/Entity Type

Executive training/business coaching

Number of Pages Required

5+ page

Colors

Designer to choose colors to be used in the design.

```html
<!DOCTYPE html>
<html lang="en">
<head>
<meta charset="utf-8">
<title>Morvenna Enterprise</title>
<link rel="stylesheet" href="https://fonts.googleapis.com/css2?family=League+Spartan:wght@300;400;500&family=Oswald:wght@500&display=swap">
<style>
:root{
  --black:#0a0808;
  --band:#1f2021;
  --footer:#2a2a2b;
  --strip:#0d0c0c;
  --orange:#ff6624;
  --white:#ffffff;
  --field:#f2f5fa;
}
*{margin:0;padding:0;box-sizing:border-box}
html,body{width:1200px;height:3098px;overflow:hidden;background:var(--black)}
body{position:relative;font-family:"League Spartan",sans-serif;color:var(--white)}
.abs{position:absolute}
a{color:inherit;text-decoration:none}
.nowrap{white-space:nowrap}

/* hero */
.hero-photo{left:194px;top:0;width:1006px;height:529px;
  background:linear-gradient(100deg,#4a4440 0%,#7d7570 35%,#a59b94 60%,#8a7f79 80%,#5b524e 100%)}
.hero-photo::after{content:"";position:absolute;inset:0;background:linear-gradient(90deg,rgba(0,0,0,.45),rgba(0,0,0,.05))}
.logo-box{left:109px;top:0;width:252px;height:79px;background:var(--black);display:flex;align-items:center;padding-left:1px}
.logo-box span{font-size:26px;font-weight:400;letter-spacing:.2px;white-space:nowrap}
.nav{top:42px;font-size:17px;font-weight:400}
.nav a{position:absolute;white-space:nowrap}
.btn-contact{left:949px;top:32px;width:140px;height:43px;background:var(--orange);display:flex;align-items:center;justify-content:center;font-size:17px}
.hero-title{left:278px;top:190px;font-size:34px;font-weight:300;line-height:42.5px;white-space:nowrap}
.btn-outline{border:1.5px solid var(--white);display:flex;align-items:center;justify-content:center;font-size:17px;font-weight:400;white-space:nowrap}
.hero-book{left:278px;top:396px;width:158px;height:43px}
.hero-dot{width:6px;height:6px;border-radius:50%;background:var(--orange)}
.hero-arrow{left:565px;top:495px}

/* side labels */
.side-tab{left:26px;width:35px;border:1.5px solid var(--orange);display:flex;align-items:center;justify-content:center}
.side-tab span{transform:rotate(-90deg);white-space:nowrap;font-family:"Oswald",sans-serif;font-weight:500;font-size:14px;color:var(--orange);letter-spacing:.5px}

/* welcome */
.welcome-title{left:278px;top:628px;font-size:34px;font-weight:300;line-height:38px;white-space:nowrap}
.welcome-text{left:638px;top:630px;font-size:17px;font-weight:300;line-height:26.5px;white-space:nowrap}
.discover{left:638px;top:773px;width:159px;height:43px}

/* services */
.services-band{left:0;top:904px;width:1200px;height:1318px;background:var(--band)}
.ph-1{left:109px;top:872px;width:478px;height:353px;background:linear-gradient(120deg,#d8dde2,#9aa4ad 55%,#3a3f48)}
.ph-2{left:613px;top:1252px;width:476px;height:299px;background:linear-gradient(135deg,#2e3a52,#cfd6de 50%,#8b97a6)}
.ph-3{left:109px;top:1579px;width:478px;height:352px;background:linear-gradient(160deg,#b7a596,#e1ddd6 45%,#5b5c66)}
.ph-4{left:613px;top:1959px;width:476px;height:299px;background:linear-gradient(120deg,#3c4148,#8c929a 50%,#4a4f57)}
.svc-title{font-size:28px;font-weight:400;letter-spacing:.3px;white-space:nowrap}
.svc-text{font-size:15.5px;font-weight:300;line-height:21.3px;white-space:nowrap}
.plus{width:19px;height:19px;background:var(--orange);display:flex;align-items:center;justify-content:center}
.learn{left:633px;top:1140px;display:flex;align-items:center;gap:12px;font-size:15px}

/* approach */
.approach{left:0;top:2347px;width:1200px;height:220px;background:var(--orange)}
.approach-title{left:109px;top:2406px;font-size:36px;font-weight:300;white-space:nowrap}
.approach-text{left:109px;top:2456px;font-size:19px;font-weight:300;line-height:21px;white-space:nowrap}
.approach-btn{left:922px;top:2436px;width:167px;height:42px}

/* footer */
.footer{left:0;top:2567px;width:1032px;height:531px;background:linear-gradient(135deg,#2f2f30,#262627 60%,#2c2c2d)}
.footer-strip{left:1032px;top:2567px;width:168px;height:531px;background:var(--strip)}
.footer-title{top:2628px;font-size:28px;font-weight:400;white-space:nowrap}
.contact-line{left:109px;display:flex;align-items:flex-start;gap:12px;font-weight:300;white-space:nowrap}
.useful{left:109px;top:2866px;color:var(--orange);font-size:19px;font-weight:300}
.links{left:109px;top:2910px;font-size:15px;font-weight:300;line-height:21px;white-space:nowrap}
.copy{left:108px;top:2999px;font-size:15px;font-weight:300;white-space:nowrap}
.field{left:529px;width:476px;background:var(--field);color:#333;font-size:14px;padding:11px 17px 0}
.send{left:529px;top:2993px;width:106px;height:42px;background:var(--orange);display:flex;align-items:center;justify-content:center;font-size:17px}
.social{left:1053px;width:35px;height:35px;border:1.5px solid var(--orange);display:flex;align-items:center;justify-content:center}
.social i{width:9px;height:9px;background:var(--orange);display:block}
.social.active{background:var(--orange)}
.social.active i{background:var(--white)}
</style>
</head>
<body>

<!-- hero -->
<div class="abs hero-photo" role="img" aria-label="Photo of a young professional woman working on a laptop at a meeting table"></div>
<div class="abs logo-box"><span>Morvenna Enterprise</span></div>
<nav class="abs nav" style="left:0;width:1200px">
  <a style="left:505px">Home</a>
  <a style="left:604px">Works</a>
  <a style="left:705px">Expertise</a>
  <a style="left:830px">About Us</a>
</nav>
<a class="abs btn-contact">Contact Us</a>

<h1 class="abs hero-title" style="font-weight:300">We help make strategy happen by<br>delivering long-term performance improvements<br>so companies can<br>"Become the change they wish to see."</h1>
<a class="abs btn-outline hero-book">Book a Service</a>

<span class="abs hero-dot" style="left:136px;top:389px"></span>
<span class="abs hero-dot" style="left:136px;top:421px"></span>
<span class="abs hero-dot" style="left:136px;top:454px"></span>
<svg class="abs" style="left:125px;top:475px" width="28" height="28" viewBox="0 0 28 28"><rect x="5" y="5" width="18" height="18" transform="rotate(45 14 14)" fill="none" stroke="#ff6624" stroke-width="1.5"/><circle cx="14" cy="14" r="2.5" fill="#ff6624"/></svg>

<svg class="abs hero-arrow" width="68" height="68" viewBox="0 0 68 68"><rect x="10" y="10" width="48" height="48" transform="rotate(45 34 34)" fill="#ff6624"/><path d="M34 27v13M29 35l5 5 5-5" fill="none" stroke="#fff" stroke-width="1.6"/></svg>

<!-- welcome -->
<div class="abs side-tab" style="top:618px;height:158px"><span>ABOUT US</span></div>
<h2 class="abs welcome-title" style="font-weight:300">Welcome to<br>Morvenna Enterprise</h2>
<p class="abs welcome-text">Morvenna Enterprise specialise in helping clients<br>make strategy happen by delivering &nbsp;long-term<br>performance improvements so they can "become the<br>change they wish to see."</p>
<a class="abs btn-outline discover">Discover More</a>

<!-- services -->
<div class="abs services-band"></div>
<div class="abs side-tab" style="top:968px;height:159px"><span>SERVICES</span></div>

<div class="abs ph-1" role="img" aria-label="Photo of a consultant presenting at a flipchart to a seated team"></div>
<h3 class="abs svc-title" style="left:638px;top:966px">Leadership &amp; Ccpability</h3>
<p class="abs svc-text" style="left:638px;top:1021px">There is a pressing need for leadership to be distributed across<br>organisations in support of constant innovation and change. For<br>businesses that believe there is a &nbsp;benefit in investing in their<br>core resource – people, we can help you gain...</p>
<div class="abs learn">
  <svg width="28" height="28" viewBox="0 0 28 28"><rect x="6" y="6" width="16" height="16" transform="rotate(45 14 14)" fill="#ff6624"/><path d="M14 10v8M10 14h8" stroke="#fff" stroke-width="1.4"/></svg>
  <span>Learn More</span>
</div>

<h3 class="abs svc-title" style="left:108px;top:1305px">Assessment &amp; Analysis</h3>
<p class="abs svc-text" style="left:108px;top:1360px">We engage key stakeholders to identify issues, clarify direction<br>and to have conversations about those areas that really matter.<br>We help clients to commit to action, implement new business<br>strategies, plan for the future and...</p>
<span class="abs plus" style="left:110px;top:1474px"><svg width="9" height="9" viewBox="0 0 9 9"><path d="M4.5 0v9M0 4.5h9" stroke="#fff" stroke-width="1.3"/></svg></span>
<div class="abs ph-2" role="img" aria-label="Photo of colleagues reviewing charts on a tablet and paper reports"></div>

<div class="abs ph-3" role="img" aria-label="Photo of a coach leading a group discussion in a bright office"></div>
<h3 class="abs svc-title" style="left:638px;top:1652px">People &amp; Engagement</h3>
<p class="abs svc-text" style="left:638px;top:1707px">It's all about people; that is, the right people.<br>Having leaders with an ability to facilitate the<br>fulfilment of your company's purpose through your people<br>provides potential for it to &nbsp;become ...</p>
<span class="abs plus" style="left:639px;top:1831px"><svg width="9" height="9" viewBox="0 0 9 9"><path d="M4.5 0v9M0 4.5h9" stroke="#fff" stroke-width="1.3"/></svg></span>

<h3 class="abs svc-title" style="left:108px;top:1992px">Investigate &amp; Guid</h3>
<p class="abs svc-text" style="left:108px;top:2047px">Success in bussiness hinges on strategic agility as well as an<br>ability to highlight and execute actions leading to measurable<br>improvements. To help businesses to do this we will support,<br>guide and partner with clients to assess ...</p>
<span class="abs plus" style="left:110px;top:2160px"><svg width="9" height="9" viewBox="0 0 9 9"><path d="M4.5 0v9M0 4.5h9" stroke="#fff" stroke-width="1.3"/></svg></span>
<div class="abs ph-4" role="img" aria-label="Photo of two business people in suits shaking hands"></div>

<!-- approach -->
<section class="abs approach"></section>
<h2 class="abs approach-title" style="font-weight:300">A Personalised Approach</h2>
<p class="abs approach-text">Working in partnership we will learn about your business and your challenges<br>for the &nbsp;purpose of designing a programme appropriate to your situation.</p>
<a class="abs btn-outline approach-btn">Book a Service</a>

<!-- footer -->
<footer class="abs footer"></footer>
<div class="abs footer-strip"></div>
<div class="abs side-tab" style="top:2630px;height:156px"><span>CONTACT US</span></div>

<h2 class="abs footer-title" style="left:108px;font-weight:400">Morvenna Enterprise</h2>
<div class="abs contact-line" style="top:2696px;font-size:22px">
  <svg width="18" height="18" viewBox="0 0 24 24" style="margin-top:3px"><path d="M6.6 10.8a15 15 0 0 0 6.6 6.6l2.2-2.2c.3-.3.7-.4 1-.2 1.1.4 2.3.6 3.6.6.6 0 1 .4 1 1V20c0 .6-.4 1-1 1A17 17 0 0 1 3 4c0-.6.4-1 1-1h3.5c.6 0 1 .4 1 1 0 1.3.2 2.5.6 3.6.1.3 0 .7-.2 1z" fill="#fff"/></svg>
  <span>123-456-7890</span>
</div>
<div class="abs contact-line" style="top:2743px;font-size:17px">
  <svg width="17" height="15" viewBox="0 0 24 20" style="margin-top:1px"><path d="M1 7l11-6 11 6v12H1z" fill="#fff"/><path d="M1 7l11 7 11-7" fill="none" stroke="#2a2a2b" stroke-width="1.6"/></svg>
  <span>info@morvennaenterprise.com</span>
</div>
<div class="abs contact-line" style="top:2787px;font-size:15px;line-height:21px">
  <svg width="15" height="19" viewBox="0 0 16 22" style="margin-top:1px;margin-left:1px"><path d="M8 0a8 8 0 0 1 8 8c0 6-8 14-8 14S0 14 0 8a8 8 0 0 1 8-8z" fill="#fff"/><circle cx="8" cy="8" r="3" fill="#2a2a2b"/></svg>
  <span style="margin-left:1px">8-40 North Lorem Ipsum,<br>&nbsp;Road Halden, marvin Work<br>&nbsp;M7R 4J9</span>
</div>
<h4 class="abs useful" style="font-weight:300">Useful Links</h4>
<p class="abs links">Terms &amp; Conditions &nbsp;&nbsp; I &nbsp;&nbsp; Cookie policy<br>Privacy policy &nbsp;&nbsp; I &nbsp;&nbsp; Sitemap</p>
<p class="abs copy">©2022 Morvenna Enterprise All Right Reserved.</p>

<h2 class="abs footer-title" style="left:529px;font-weight:400">Request a Quote</h2>
<div class="abs field" style="top:2698px;height:34px">Your Name</div>
<div class="abs field" style="top:2746px;height:34px">Email</div>
<div class="abs field" style="top:2795px;height:34px">Phone</div>
<div class="abs field" style="top:2844px;height:121px">Type your message</div>
<a class="abs send">Send</a>

<svg class="abs" style="left:1111px;top:2625px" width="68" height="68" viewBox="0 0 68 68"><rect x="10" y="10" width="48" height="48" transform="rotate(45 34 34)" fill="#ff6624"/><path d="M34 41V28M29 33l5-5 5 5" fill="none" stroke="#fff" stroke-width="1.6"/></svg>

<a class="abs social" style="top:2869px" aria-label="Social link one"><i></i></a>
<a class="abs social active" style="top:2913px" aria-label="Social link two"><i></i></a>
<a class="abs social" style="top:2958px" aria-label="Social link three"><i></i></a>
<a class="abs social" style="top:3002px" aria-label="Social link four"><i></i></a>

</body>
</html>
```